Vacation Rental Postcard Design

The Kestrel's Perch is a vacation rental cottage. We want a postcard that can be used as promotional give-aways for visitors as well as something that can be given to the tourism board and local merchants to help us promote the rental.

Our tag line is" The Kestrel's Perch - the finest perch on the ridge!". Should also include "Snohomish, WA USA"

We have also used "Come see what all of the buzz is about"

Want to include our info in small print on the mailing side portion of the postcard:

STAYQ: www.stayqlet.com/417295
Friendloop: www.friendloop.com/thefinestperchontheridge

Target Market(s)

Couples, romantic, honeymooners, coming for wine tasting, hot air ballooning, hiking, enjoying nature

Industry/Entity Type

Tourism

```html
<!DOCTYPE html>
<html lang="en">
<head>
<meta charset="utf-8">
<title>The Kestrel's Perch – Postcard</title>
<link href="https://fonts.googleapis.com/css2?family=Bebas+Neue&display=swap" rel="stylesheet">
<style>
  :root {
    --page: #ffffff;
    --card: #ffffff;
    --ink: #1a1a1a;
    --rule: #555555;
    --guide: #cfcfcf;
    --shadow: rgba(0,0,0,0.12);
  }
  * { box-sizing: border-box; margin: 0; padding: 0; }
  html, body { width: 748px; height: 1200px; overflow: hidden; background: var(--page); }
  .canvas { position: relative; width: 748px; height: 1200px; font-family: "Bebas Neue", "Arial Narrow", sans-serif; color: var(--ink); }

  .postcard {
    position: absolute; left: 37px; width: 678px; height: 524px;
    background: var(--card); box-shadow: 0 4px 12px var(--shadow);
  }
  .postcard--mailing { top: 51px; }
  .postcard--photos { top: 636px; }

  .trim-guides { position: absolute; inset: 0; width: 100%; height: 100%; pointer-events: none; }
  .trim-guides line { stroke: var(--guide); stroke-width: 1.2; stroke-dasharray: 6 5; }

  /* Mailing side */
  .tagline { position: absolute; left: 45px; top: 60px; font-size: 21px; line-height: 22px; letter-spacing: 0.2px; }
  .message-lines { position: absolute; left: 42px; top: 152px; width: 311px; }
  .message-lines .lead { width: 166px; height: 2px; background: var(--rule); margin-bottom: 22px; }
  .message-lines .line { height: 2px; background: var(--rule); margin-bottom: 20.8px; }

  .contact-strip {
    position: absolute; left: 407px; top: 52px; width: 18px; height: 458px;
  }
  .contact-strip span {
    position: absolute; left: 0; bottom: 0; white-space: nowrap;
    transform: rotate(-90deg); transform-origin: 0 0;
    translate: 0 0; font-size: 12.5px; letter-spacing: 0.3px;
    width: 458px; text-align: center; top: 458px;
  }

  .stamp-box { position: absolute; left: 537px; top: 52px; width: 94px; height: 115px; border: 2px solid var(--ink); }

  .brand-mark { position: absolute; left: 500px; top: 228px; width: 150px; text-align: center; }
  .brand-mark .dot { width: 56px; height: 56px; border-radius: 50%; background: var(--ink); margin: 0 auto 8px; }
  .brand-mark .name { font-size: 19px; line-height: 20px; }

  .address-lines { position: absolute; left: 463px; top: 400px; width: 170px; }
  .address-lines .line { height: 2px; background: var(--rule); margin-bottom: 24px; }

  /* Photo side */
  .photo-grid {
    position: absolute; left: 21px; top: 26px;
    display: grid; grid-template-columns: repeat(3, 208px); grid-template-rows: repeat(3, 155px); gap: 6px;
  }
  .photo { display: block; }
  .photo--living { background: linear-gradient(160deg, #c9b48a 0%, #7a4a2a 55%, #3a2418 100%); }
  .photo--bedroom { background: linear-gradient(180deg, #b8902e 0%, #d9cfb8 60%, #5b6b3e 100%); }
  .photo--sunset { background: linear-gradient(180deg, #d96a8a 0%, #f08a6a 45%, #3a2630 75%, #1a1418 100%); }
  .photo--rainbow { background: linear-gradient(180deg, #7d7f90 0%, #9a9cab 45%, #3e5a32 70%, #5f8a3e 100%); }
  .photo--lounge { background: linear-gradient(170deg, #b88a3c 0%, #6b4422 55%, #2e1c12 100%); }
  .photo--garden { background: linear-gradient(180deg, #5c8fd6 0%, #b9cde8 35%, #4e6e34 65%, #7a8a5a 100%); }
  .photo--balloons { background: linear-gradient(180deg, #3f7fd0 0%, #8cb6e6 50%, #5f8a2e 75%, #3f6a20 100%); }
  .photo--autumn { background: linear-gradient(180deg, #9aa2a6 0%, #7e9a5a 45%, #c47a2a 80%, #8a4a1a 100%); }
  .photo--cottage { background: linear-gradient(180deg, #3c6a3a 0%, #284a36 50%, #8a6a5a 80%, #6a7a4a 100%); }
</style>
</head>
<body>
<div class="canvas">

  <section class="postcard postcard--mailing" aria-label="Mailing side">
    <h1 class="tagline">The Kestrel's Perch<br>- The finest perch on the ridge!</h1>

    <div class="message-lines" aria-hidden="true">
      <div class="lead"></div>
      <div class="line"></div><div class="line"></div><div class="line"></div><div class="line"></div>
      <div class="line"></div><div class="line"></div><div class="line"></div><div class="line"></div>
      <div class="line"></div><div class="line"></div><div class="line"></div><div class="line"></div>
      <div class="line"></div>
    </div>

    <div class="contact-strip">
      <span>www.stayqlet.com/417295 &nbsp;•&nbsp; www.friendloop.com/thefinestperchontheridge</span>
    </div>

    <div class="stamp-box" aria-label="Stamp area"></div>

    <div class="brand-mark">
      <div class="dot"></div>
      <div class="name">The Kestrel's Perch</div>
    </div>

    <div class="address-lines" aria-hidden="true">
      <div class="line"></div><div class="line"></div><div class="line"></div>
    </div>

    <svg class="trim-guides" viewBox="0 0 678 524" preserveAspectRatio="none" aria-hidden="true">
      <line x1="0" y1="0" x2="678" y2="524"/>
      <line x1="678" y1="0" x2="0" y2="524"/>
    </svg>
  </section>

  <section class="postcard postcard--photos" aria-label="Photo side">
    <div class="photo-grid">
      <div class="photo photo--living" role="img" aria-label="Photo: living room with dining table and flowers"></div>
      <div class="photo photo--bedroom" role="img" aria-label="Photo: bedroom with white quilted bed"></div>
      <div class="photo photo--sunset" role="img" aria-label="Photo: pink sunset over evergreen trees"></div>
      <div class="photo photo--rainbow" role="img" aria-label="Photo: rainbow over a green meadow"></div>
      <div class="photo photo--lounge" role="img" aria-label="Photo: lounge with sofa and wood floor"></div>
      <div class="photo photo--garden" role="img" aria-label="Photo: garden path with roses and valley view"></div>
      <div class="photo photo--balloons" role="img" aria-label="Photo: hot air balloons on a field"></div>
      <div class="photo photo--autumn" role="img" aria-label="Photo: autumn garden and patio"></div>
      <div class="photo photo--cottage" role="img" aria-label="Photo: green cottage exterior with porch"></div>
    </div>

    <svg class="trim-guides" viewBox="0 0 678 524" preserveAspectRatio="none" aria-hidden="true">
      <line x1="0" y1="0" x2="678" y2="524"/>
      <line x1="678" y1="0" x2="0" y2="524"/>
    </svg>
  </section>

</div>
</body>
</html>
```